Zentrix Banner Grid Ads for Custom Software Company

We need some images for display on the Zentrix Banner Grid. Need a collection of them at different sizes.

This is for a custom software development company that specializes in small to medium size businesses.

PLEASE PLEASE PLEASE GET CREATIVE! That is the point! Something very typical and plain will not win!

Target Market(s)

Small and Medium sized businesses looking for custom software development services

Industry/Entity Type

Computer Software

Font styles to use
Serif
Sans Serif

Requirements
Must have
• Medium Rectangle (300×250)
• Large Rectangle (336×280)
• Leaderboard (728×90)
• Half Page (300×600)
• Large Mobile Banner (320×100)
• Needs to stand out, but not be obnoxious
• Needs to flow with the website design and colors (does not need to be the same colors, just needs to work together)
• Must have specific call to action (schedule appointment or read more are options, but feel free to make up more)
Nice to have
• Logo integration
• Adobe Illustrator files with artboards/exports for the different sizes
Should not have
• Should not have more than 20% text
• Don't steal from the slides on the website. We want "read more" to mean read more, not more of the same.

```html
<!DOCTYPE html>
<html lang="en">
<head>
<meta charset="UTF-8">
<title>Velmora Software – Outstanding Result</title>
<link rel="stylesheet" href="https://fonts.googleapis.com/css2?family=Montserrat:wght@600;700;800&display=swap">
<style>
  :root {
    --teal: #4fb9c5;
    --teal-light: #5fc3cd;
    --navy: #1b2370;
    --navy-deep: #141b5a;
    --white: #ffffff;
    --brand-blue: #1f5f99;
    --cta-red: #d8262f;
    --glow-warm: rgba(244, 162, 58, 0.55);
    --glow-light: rgba(233, 238, 245, 0.75);
  }
  * { margin: 0; padding: 0; box-sizing: border-box; }
  html, body { width: 1200px; height: 148px; overflow: hidden; background: var(--teal); }
  .banner {
    position: relative;
    width: 1200px;
    height: 148px;
    overflow: hidden;
    background: linear-gradient(90deg, var(--teal) 0%, var(--teal-light) 55%, var(--teal) 100%);
    font-family: "Montserrat", Arial, sans-serif;
  }
  .brand-panel {
    position: absolute;
    left: 0; top: 0;
    width: 247px; height: 96px;
    background: var(--white);
    border-bottom-right-radius: 10px;
    display: flex;
    align-items: center;
    padding-left: 20px;
    gap: 10px;
  }
  .brand-mark { width: 22px; height: 22px; background: var(--brand-blue); flex: none; }
  .brand-name { font-weight: 600; font-size: 20px; color: var(--brand-blue); line-height: 1.1; white-space: nowrap; }
  .message {
    position: absolute;
    left: 160px;
    width: 750px;
    top: 54px;
    text-align: center;
    color: var(--white);
    font-weight: 800;
    text-transform: uppercase;
    white-space: nowrap;
  }
  .headline { font-size: 38px; line-height: 1; letter-spacing: 0.3px; }
  .tagline { font-size: 23px; line-height: 1; margin-top: 14px; letter-spacing: 0.4px; }
  .orbit { position: absolute; left: 1047px; top: -16px; width: 180px; height: 180px; }
  .rocket-art {
    position: absolute;
    left: 870px; top: 28px;
    width: 250px; height: 90px;
    border-radius: 50%;
    background: radial-gradient(ellipse at 65% 50%, var(--glow-light) 0%, var(--glow-warm) 45%, rgba(244,162,58,0) 72%);
  }
  .cta {
    position: absolute;
    left: 1072px; top: 108px;
    padding: 7px 14px;
    border-radius: 16px;
    background: var(--cta-red);
    color: var(--white);
    font-weight: 700;
    font-size: 13px;
    letter-spacing: 0.6px;
    text-transform: uppercase;
    text-decoration: none;
    white-space: nowrap;
  }
</style>
</head>
<body>
<main class="banner">
  <div class="brand-panel">
    <span class="brand-mark"></span>
    <span class="brand-name">Velmora Software</span>
  </div>

  <div class="message">
    <p class="headline">Outstanding Result</p>
    <p class="tagline">We set the record straight from the start</p>
  </div>

  <svg class="orbit" viewBox="0 0 180 180" aria-hidden="true">
    <circle cx="90" cy="90" r="90" fill="var(--navy)"/>
    <circle cx="90" cy="90" r="60" fill="var(--navy-deep)"/>
  </svg>

  <div class="rocket-art" role="img" aria-label="Illustration of a white and red cartoon rocket flying right with a flame trail"></div>

  <a class="cta" href="#">Read More</a>
</main>
</body>
</html>
```